tri-fold brochure design for psychology practice - all content provided

we are a psychology practice that specialises in learning & wellbeing clinic for children, adolescents and adults. We have an existing logo and I am attaching a word doc (tri-fold brochure) with the required content. I am also attaching our logo and other relevant content docs. The layout is only a sample and we are looking for someone to put this together into a consistent and better layout.

Target Market(s)

parents

Industry/Entity Type

education and health

Font styles to use
Other font styles liked:
• crimsonpro

Requirements
Must have
• our logo and the provided content

```html
<!DOCTYPE html>
<html lang="en">
<head>
<meta charset="utf-8">
<title>Meridian Psychology – tri-fold brochure</title>
<link href="https://fonts.googleapis.com/css2?family=Montserrat:wght@500;600;700&family=Arimo:wght@400;700&display=swap" rel="stylesheet">
<style>
  :root {
    --stage: #5b5b5b;
    --label: #d6d6d6;
    --green: #5a9a3c;
    --green-dark: #4c8a31;
    --green-bright: #5bbf72;
    --blue: #4a8fd6;
    --ink: #333333;
    --ink-soft: #555555;
    --paper: #ffffff;
    --paper-grey: #eeefec;
    --footer-grey: #dcdcd8;
  }
  * { box-sizing: border-box; margin: 0; padding: 0; }
  html, body { width: 1200px; height: 4183px; overflow: hidden; }
  body { background: var(--stage); font-family: "Arimo", Arial, sans-serif; color: var(--ink); position: relative; }

  .spread-label { position: absolute; left: 130px; font-family: "Montserrat", sans-serif; font-size: 17px; letter-spacing: 4px; color: var(--label); font-weight: 500; }
  .spread { position: absolute; left: 91px; width: 1018px; height: 714px; display: flex; box-shadow: 0 6px 18px rgba(0,0,0,.35); }
  .panel { position: relative; width: 340px; height: 100%; background: var(--paper); text-align: center; }
  .panel--grey { background: linear-gradient(90deg, #e6e7e3, var(--paper-grey) 40%, #f6f6f4); }

  .brand { display: flex; flex-direction: column; align-items: center; }
  .brand-row { display: flex; align-items: center; gap: 8px; }
  .brand-mark { width: 12px; height: 12px; background: var(--ink); }
  .brand-name { font-family: "Montserrat", sans-serif; font-weight: 600; font-size: 24px; color: var(--ink); line-height: 1; }
  .brand-tag { font-family: "Arimo", sans-serif; font-size: 11px; color: var(--ink-soft); margin-top: 6px; letter-spacing: .5px; }

  .url { font-size: 11px; color: var(--ink-soft); }
  .url b { color: var(--green-dark); }

  .step { position: absolute; left: 42px; width: 256px; border: 1.5px solid var(--blue); border-radius: 4px; padding: 34px 12px 12px; font-size: 11px; line-height: 1.5; color: var(--ink); }
  .step h3 { font-family: "Montserrat", sans-serif; font-size: 14px; font-weight: 600; margin-bottom: 8px; }
  .step--blue h3 { color: var(--blue); }
  .step--green { border-color: var(--green-bright); }
  .step--green h3 { color: var(--green); }
  .step-icon { position: absolute; left: 50%; top: -28px; margin-left: -28px; width: 56px; height: 56px; border-radius: 50%; display: flex; align-items: center; justify-content: center; }
  .step-icon--blue { background: var(--blue); }
  .step-icon--green { background: var(--green); }
  .connector { position: absolute; left: 169px; width: 2px; background: var(--blue); }

  .branch-art { position: absolute; background: linear-gradient(100deg, rgba(91,65,48,.18), rgba(140,193,82,.35) 55%, rgba(91,65,48,.15)); border-radius: 40% 55% 45% 60%; }

  .contact-icons { position: absolute; top: 495px; left: 0; right: 0; display: flex; justify-content: center; gap: 14px; }
  .contact-icons span { width: 24px; height: 24px; border-radius: 50%; background: var(--green); display: flex; align-items: center; justify-content: center; }
  .contact-lines { position: absolute; top: 548px; left: 0; right: 0; font-size: 15px; line-height: 1.45; color: var(--ink); }

  .headline-band { position: absolute; top: 540px; left: 0; right: 0; height: 120px; background: var(--green); display: flex; align-items: center; justify-content: center; }
  .headline-band h1 { font-family: "Montserrat", sans-serif; font-weight: 600; font-size: 25px; line-height: 1.25; color: #fff; letter-spacing: .5px; }

  .bottom-url { position: absolute; bottom: 22px; left: 0; right: 0; }

  .photo { position: absolute; top: 132px; left: 0; right: 0; height: 266px; background: linear-gradient(135deg, #f2ede6, #d9c7b4 55%, #b98c6a); }
  .pill { display: inline-block; font-family: "Montserrat", sans-serif; font-weight: 600; color: #fff; padding: 4px 14px; border-radius: 6px; }
  .pill--green { background: var(--green-bright); font-size: 17px; }
  .pill--blue { background: var(--blue); font-size: 16px; }
  .body-copy { font-size: 11.5px; line-height: 1.45; color: var(--ink); }
  .body-copy p + p { margin-top: 14px; }
  .foot-band { position: absolute; bottom: 0; left: 0; right: 0; height: 56px; display: flex; align-items: center; justify-content: center; font-size: 11.5px; }
  .foot-band--green { background: var(--green-bright); color: #fff; }
  .foot-band--grey { background: var(--footer-grey); color: var(--ink-soft); }

  .conditions { list-style: none; text-align: left; margin: 28px auto 0; width: 250px; }
  .conditions li { position: relative; padding: 4px 0 4px 30px; font-family: "Montserrat", sans-serif; font-weight: 600; font-size: 12.5px; line-height: 1.3; }
  .conditions li:nth-child(odd) { background: linear-gradient(90deg, rgba(255,255,255,.8), transparent); }
  .conditions li::before { content: ""; position: absolute; left: 6px; top: 8px; border-left: 8px solid var(--green-bright); border-top: 5px solid transparent; border-bottom: 5px solid transparent; }

  .process-step { position: absolute; left: 58px; width: 262px; height: 80px; border: 1.5px dashed var(--green-bright); border-radius: 4px; padding: 12px 8px 8px 46px; text-align: left; font-size: 10.5px; line-height: 1.35; color: var(--ink); }
  .process-num { position: absolute; left: -30px; top: 50%; margin-top: -30px; width: 60px; height: 60px; border-radius: 50%; background: var(--green-bright); border: 4px solid #fff; box-shadow: 0 0 0 1.5px var(--green-bright); color: #fff; font-family: "Montserrat", sans-serif; font-weight: 600; font-size: 26px; display: flex; align-items: center; justify-content: center; }
</style>
</head>
<body>

<div class="spread-label" style="top:2558px">BROCHURE_OUTSIDE</div>
<section class="spread" style="top:2600px" aria-label="Brochure outside">
  <div class="panel">
    <div class="step step--blue" style="top:72px; height:146px">
      <div class="step-icon step-icon--blue">
        <svg width="30" height="30" viewBox="0 0 30 30" fill="none" stroke="#fff" stroke-width="1.6"><circle cx="15" cy="9" r="4"/><circle cx="8" cy="19" r="3"/><circle cx="22" cy="19" r="3"/><path d="M3 28c0-3 2-5 5-5s5 2 5 5M17 28c0-3 2-5 5-5s5 2 5 5"/></svg>
      </div>
      <h3>UNDERSTANDING</h3>
      Assessment starts with listening first, and then asking the right questions in order to ensure that we are understanding your concerns and hearing your questions.
    </div>
    <div class="connector" style="top:220px; height:40px"></div>
    <div class="step step--green" style="top:288px; height:152px">
      <div class="step-icon step-icon--green">
        <svg width="30" height="30" viewBox="0 0 30 30" fill="none" stroke="#fff" stroke-width="2.4"><circle cx="13" cy="13" r="7"/><path d="M18 18l7 7"/></svg>
      </div>
      <h3>IDENTIFYING</h3>
      It is then our job to use our diagnostic and assessment knowledge and skills to collect the right data in order to address your concerns and provide answers to your questions.
    </div>
    <div class="connector" style="top:442px; height:42px; background:var(--green-bright)"></div>
    <div class="step step--green" style="top:512px; height:148px">
      <div class="step-icon step-icon--green">
        <svg width="30" height="30" viewBox="0 0 30 30" fill="none" stroke="#fff" stroke-width="2"><path d="M15 4v24"/><path d="M15 7h8l3 3-3 3h-8z" fill="#fff"/><path d="M15 15H8l-3 3 3 3h7z"/></svg>
      </div>
      <h3>GUIDING</h3>
      This then enables us to provide you with recommendations for accessing support and interventions that are based on current best practice and are supported by evidence.
    </div>
    <div class="bottom-url url">www.<b>meridianpsych</b>.com.au</div>
  </div>

  <div class="panel panel--grey">
    <div class="brand" style="padding-top:74px">
      <div class="brand-row"><span class="brand-mark"></span><span class="brand-name">Meridian Psychology</span></div>
      <div class="brand-tag">learning &amp; wellbeing clinic</div>
    </div>
    <div class="contact-icons">
      <span><svg width="12" height="12" viewBox="0 0 12 12"><path d="M6 1a3.5 3.5 0 0 1 3.5 3.5C9.5 7 6 11 6 11S2.5 7 2.5 4.5A3.5 3.5 0 0 1 6 1z" fill="#fff"/><circle cx="6" cy="4.5" r="1.2" fill="#5a9a3c"/></svg></span>
      <span><svg width="12" height="12" viewBox="0 0 12 12"><path d="M3 1l2 2.5-1 1.2c.6 1.3 1.6 2.3 2.9 2.9l1.2-1L10.6 8.6 9.4 10.8C5.5 10.4 1.6 6.5 1.2 2.6z" fill="#fff"/></svg></span>
      <span><svg width="12" height="12" viewBox="0 0 12 12" fill="none" stroke="#fff" stroke-width="1.2"><rect x="1.5" y="3" width="9" height="6.5" fill="#fff"/><path d="M1.5 3l4.5 3.5L10.5 3" stroke="#5a9a3c"/></svg></span>
      <span><svg width="12" height="12" viewBox="0 0 12 12" fill="none" stroke="#fff" stroke-width="1"><circle cx="6" cy="6" r="4.8"/><ellipse cx="6" cy="6" rx="2" ry="4.8"/><path d="M1.2 6h9.6"/></svg></span>
    </div>
    <div class="contact-lines">
      12/48 Harbour View Rd,<br>Dee Why NSW 2099<br>02 9000 4417<br>hello@meridianpsych.com.au<br>www.meridianpsych.com.au
    </div>
  </div>

  <div class="panel">
    <div class="brand" style="padding-top:74px">
      <div class="brand-row"><span class="brand-mark"></span><span class="brand-name">Meridian Psychology</span></div>
      <div class="brand-tag">learning &amp; wellbeing clinic</div>
    </div>
    <div class="headline-band"><h1>UNDERSTANDING<br>IDENTIFYING<br>GUIDING</h1></div>
    <div class="bottom-url url">www.<b>meridianpsych</b>.com.au</div>
  </div>

  <div class="branch-art" role="img" aria-label="Illustration of a brown tree branch with green leaves stretching across the cover panels" style="left:340px; top:185px; width:678px; height:290px"></div>
</section>

<div class="spread-label" style="top:3358px">BROCHURE_INSIDE</div>
<section class="spread" style="top:3400px" aria-label="Brochure inside">
  <div class="panel">
    <div class="brand" style="padding-top:44px">
      <div class="brand-row"><span class="brand-mark"></span><span class="brand-name">Meridian Psychology</span></div>
      <div class="brand-tag">learning &amp; wellbeing clinic</div>
    </div>
    <div class="photo" role="img" aria-label="Photo of a smiling woman in glasses reading a book with a young boy at a table"></div>
    <div style="position:absolute; top:418px; left:0; right:0"><span class="pill pill--green">WHO WE ARE</span></div>
    <div class="body-copy" style="position:absolute; top:460px; left:30px; right:30px">
      <p>Meridian Psychology is a team with a passion for helping people to thrive. We are a team of psychologists and teachers who have experience in both educational and clinical settings.</p>
      <p>We understand the challenges parents face in wanting what is best for their children, trying to understand how and where to access the most relevant information and support.</p>
    </div>
    <div class="foot-band foot-band--green">Call : 02 9000 4417</div>
  </div>

  <div class="panel panel--grey">
    <div class="body-copy" style="padding:40px 36px 0">
      <p>We are passionate about wanting to help families navigate the diagnostic and assessment process.</p>
      <p>We believe that quality and comprehensive assessment needs to happen before intervention begins. We work collaboratively with other professionals to ensure that recommendations and supports put in place are appropriate and evidence-based while also meeting the needs of the individual.</p>
      <p>We are qualified to give formal diagnoses for mental health conditions and specific learning disorders. This includes:</p>
    </div>
    <ul class="conditions">
      <li>Attention Deficit<br>Hyperactivity Disorder</li>
      <li>Autism Spectrum Disorder</li>
      <li>Specific Learning Disorders</li>
      <li>Language disorders</li>
      <li>Anxiety Disorders</li>
      <li>Mood Disorders</li>
      <li>Communication Disorders</li>
    </ul>
    <div class="body-copy" style="position:absolute; top:560px; left:36px; right:36px">
      <p>We are passionate about collaborating with your school or workplace, supporting you in applying for financial support if available (such as NDIS funding), and to feel more informed and confident in your decisions.</p>
    </div>
    <div class="foot-band foot-band--grey">www.<b style="color:#333333">meridianpsych</b>.com.au</div>
  </div>

  <div class="panel">
    <div style="padding-top:34px"><span class="pill pill--blue">THE PROCESS</span></div>
    <div class="process-step" style="top:86px"><span class="process-num">1</span>An initial face-to-face interview to discuss your concerns and understand the relevant history and details.</div>
    <div class="process-step" style="top:186px"><span class="process-num">2</span>A formal assessment sessions during which relevant tests are completed. This can include IQ testing, Achievement testing, Memory testing, Personality profiling etc.</div>
    <div class="process-step" style="top:286px"><span class="process-num">3</span>obtaining additional information through questionnaires, observation, contact with other professionals (such as teachers/tutors etc).</div>
    <div class="process-step" style="top:386px"><span class="process-num">4</span>A feedback session during which we provide you with a final draft of the report and discuss possible recommendations, collaborating about the next steps.</div>
    <div class="process-step" style="top:486px"><span class="process-num">5</span>A copy of the finalised report is provided and opportunity for discussion and engagement with teachers or other allied health is provided.</div>
    <div class="foot-band foot-band--green">hello@meridianpsych.com.au</div>
  </div>
</section>

</body>
</html>
```